Cobalto Grande

I want a glossy card on both sides. We sell underwater LED lights for water craft

we sell custom audio enclosures for automobile, boats and atv's.

view our websites for any other pictures you may think are better suited.

Industry/Entity Type

Audio

Contact Information for Business Card

Email address: CobaltoGrande@mailvista.example
Website: www.hullglowtap.example
underwater LED lighting for watercraft
boat drain plug lights
phone number: 555-271-0648

other side of card:
email address the same
website: www.versatilesoundshells.example
speaker enclosures, auto, boat and atv
same phone number

```html
<!DOCTYPE html>
<html lang="en">
<head>
<meta charset="utf-8">
<title>Cobalto Grande – Business Card</title>
<link rel="stylesheet" href="https://fonts.googleapis.com/css2?family=Source+Sans+3:wght@400;700&display=swap">
<style>
  :root {
    --ink: #000000;
    --paper: #ffffff;
    --accent-blue: #5b7fc5;
    --photo-dark: #1c1f22;
    --photo-mid: #6f7478;
    --photo-light: #c9cccf;
  }
  html, body {
    margin: 0;
    padding: 0;
    overflow: hidden;
    background: var(--paper);
  }
  .card {
    position: relative;
    width: 1200px;
    height: 702px;
    box-sizing: border-box;
    border: 7px solid var(--ink);
    background: var(--paper);
    overflow: hidden;
    font-family: "Source Sans 3", "Gill Sans", Arial, sans-serif;
  }
  .business-name {
    position: absolute;
    left: 282px;
    top: 68px;
    margin: 0;
    font-family: "Source Sans 3", "Gill Sans", Arial, sans-serif;
    font-weight: 400;
    font-size: 118px;
    line-height: 1;
    color: var(--ink);
    white-space: nowrap;
  }
  .product-photo {
    position: absolute;
    left: 56px;
    top: 272px;
    width: 382px;
    height: 348px;
  }
  .tagline {
    position: absolute;
    left: 455px;
    top: 272px;
    margin: 0;
    font-size: 48px;
    line-height: 61px;
    color: var(--accent-blue);
    font-weight: 400;
    white-space: nowrap;
  }
  .contact-list {
    position: absolute;
    left: 504px;
    top: 432px;
    margin: 0;
    padding: 0;
    list-style: none;
  }
  .contact-item {
    display: flex;
    align-items: center;
    height: 53px;
    font-size: 36px;
    color: var(--ink);
    white-space: nowrap;
  }
  .contact-badge {
    flex: none;
    width: 33px;
    height: 33px;
    border-radius: 50%;
    background: var(--ink);
    color: var(--paper);
    font-size: 24px;
    font-weight: 700;
    line-height: 30px;
    text-align: center;
    margin-right: 25px;
  }
</style>
</head>
<body>
  <main class="card">
    <h1 class="business-name">Cobalto Grande</h1>

    <svg class="product-photo" viewBox="0 0 382 348" role="img" aria-label="Photo of a black speaker pod enclosure with a silver spoked speaker grille">
      <defs>
        <radialGradient id="podTone" cx="50%" cy="35%" r="62%">
          <stop offset="0%" stop-color="var(--photo-light)"/>
          <stop offset="45%" stop-color="var(--photo-mid)"/>
          <stop offset="100%" stop-color="var(--photo-dark)"/>
        </radialGradient>
      </defs>
      <ellipse cx="191" cy="174" rx="184" ry="166" fill="url(#podTone)"/>
    </svg>

    <p class="tagline">Speaker Enclosures for<br>Cars, Boats and ATVs</p>

    <ul class="contact-list">
      <li class="contact-item"><span class="contact-badge">e</span>CobaltoGrande@mailvista.example</li>
      <li class="contact-item"><span class="contact-badge">w</span>www.versatilesoundshells.example</li>
      <li class="contact-item"><span class="contact-badge">p</span>555-271-0648</li>
    </ul>
  </main>
</body>
</html>
```